Business Card Design

I am selling Cruelty Free/not tested on animal products.
Ideally I would like pictures of rabbits/guinea pigs/Beagle(dog)/rat/mice, as these are the main creatures that are tested on.
Background of card Earth, clouds or rainbow.
Yes I am an animal activist.
My favorite colours are purple and green.

Reason: havent got the perfect design as yet

Industry/Entity Type

Business

Contact Information for Business Card

GENTLY BY NATURE
Cruelty Free Products
Norma Faldt
0492 837 514

```html
<!DOCTYPE html>
<html lang="en">
<head>
<meta charset="utf-8">
<title>Gently By Nature – Business Card</title>
<link rel="stylesheet" href="https://fonts.googleapis.com/css2?family=Cinzel:wght@400&family=Arimo:wght@400;700&display=swap">
<style>
  :root {
    --page-bg: #ffffff;
    --sky-top: #a9c6ea;
    --sky-mid: #d3e3f5;
    --sky-low: #f2f7fc;
    --brand-purple: #5c3f98;
    --brand-green: #1f9a3c;
    --band-green: #23a146;
    --contact-green: #2fae4a;
    --contact-white: #ffffff;
    --card-shadow: rgba(0, 0, 0, 0.22);
  }

  * { box-sizing: border-box; margin: 0; padding: 0; }

  html, body {
    width: 1200px;
    height: 900px;
    overflow: hidden;
    background: var(--page-bg);
  }

  .canvas {
    position: relative;
    width: 1200px;
    height: 900px;
  }

  .business-card {
    position: absolute;
    left: 90px;
    top: 155px;
    width: 1020px;
    height: 590px;
    overflow: hidden;
    box-shadow: 0 14px 36px var(--card-shadow);
  }

  .sky-backdrop {
    position: absolute;
    inset: 0 0 auto 0;
    height: 332px;
    background:
      radial-gradient(ellipse 320px 90px at 22% 55%, rgba(255,255,255,0.85), rgba(255,255,255,0) 70%),
      radial-gradient(ellipse 380px 110px at 70% 30%, rgba(255,255,255,0.75), rgba(255,255,255,0) 70%),
      radial-gradient(ellipse 420px 90px at 55% 85%, rgba(255,255,255,0.9), rgba(255,255,255,0) 70%),
      linear-gradient(180deg, var(--sky-top) 0%, var(--sky-mid) 55%, var(--sky-low) 100%);
  }

  .brand-mark {
    position: absolute;
    left: 150px;
    top: 95px;
    width: 170px;
    height: 170px;
    border-radius: 50%;
    background: var(--brand-green);
  }

  .brand-lockup {
    position: absolute;
    left: 365px;
    top: 140px;
  }

  .brand-name {
    font-family: "Cinzel", serif;
    font-weight: 400;
    font-size: 54px;
    line-height: 1;
    color: var(--brand-purple);
    letter-spacing: 0.5px;
    white-space: nowrap;
  }

  .brand-tagline {
    margin-top: 14px;
    font-family: "Arimo", sans-serif;
    font-weight: 700;
    font-size: 30px;
    letter-spacing: 2.6px;
    color: var(--brand-green);
    white-space: nowrap;
  }

  .accent-band {
    position: absolute;
    left: 0;
    right: 0;
    top: 332px;
    height: 16px;
    background: var(--band-green);
  }

  .contact-panel {
    position: absolute;
    left: 0;
    right: 0;
    top: 348px;
    bottom: 0;
    background: var(--brand-purple);
    text-align: center;
    padding-top: 62px;
  }

  .contact-name {
    font-family: "Arimo", sans-serif;
    font-weight: 400;
    font-size: 32px;
    color: var(--contact-green);
    line-height: 1.2;
  }

  .contact-phone {
    margin-top: 8px;
    font-family: "Arimo", sans-serif;
    font-weight: 400;
    font-size: 38px;
    letter-spacing: 1px;
    color: var(--contact-white);
    line-height: 1.2;
  }
</style>
</head>
<body>
  <main class="canvas">
    <section class="business-card">
      <div class="sky-backdrop" role="img" aria-label="Soft blue sky with white clouds"></div>

      <div class="brand-mark" aria-hidden="true"></div>
      <div class="brand-lockup">
        <h1 class="brand-name">Gently By Nature</h1>
        <p class="brand-tagline">Cruelty Free Products</p>
      </div>

      <div class="accent-band"></div>

      <div class="contact-panel">
        <p class="contact-name">Norma Faldt</p>
        <p class="contact-phone">0492 837 514</p>
      </div>
    </section>
  </main>
</body>
</html>
```